Velmoor Tabletop Goods Company (southern african focus for now) needs a e-commerce website

We need a website design for a playing card company based in Southern Africa/United States. We make locally-sourced playing cards (standard 52 card deck, with customized fronts and backs) for everyone and collaborate with local artists to uplift their talents, while celebrating their nation's culture, heritage, beauty and identity. We would like to see designs that use the colours blue (see flag of Eswatini as starting product), white and some red accents (or your recommendation). The final design should communicate elegance, fun and sustainable prosperity.

Target Market(s)

Everyone loves playing cards. From the solo adventurer to the party host, first time learner or expert, young, middle and old, we need to attract a broad audience that appreciates the finer things and supports sustainable, environmentally contentiousness causes that support the local economy and uplift local talent - thing global, act local.

Number of Pages Required

4 page

Font styles to use
Serif
Sans Serif

Requirements
Must have
• Pages to include Home (Main), About (Our Story), Shop and Contact
Nice to have
• While designs may be static, elements of graceful movement would be desirable. Perhaps functionality of scrolling down on homepage showing playing cards in use, front and back. Brisk and Tolvane store's capture that elegant yet rich look.
Should not have
• Too many products. We focus on 1-2.

```html
<!DOCTYPE html>
<html lang="en">
<head>
<meta charset="utf-8">
<title>Velmoor – Playing Cards</title>
<link href="https://fonts.googleapis.com/css2?family=Alice&family=Poppins:wght@300;400;500;600&display=swap" rel="stylesheet">
<style>
:root{
  --blue:#0a7fe0;
  --blue-deep:#0c4f96;
  --card-blue:#3f5bb8;
  --ink:#1b1b1b;
  --muted:#555;
  --line:#cfcfcf;
  --white:#fff;
  --red:#d8262b;
}
*{box-sizing:border-box;margin:0;padding:0}
html,body{width:1200px;height:3855px;overflow:hidden;background:var(--white)}
body{font-family:'Poppins',sans-serif;color:var(--ink);position:relative}
.btn{display:inline-block;background:var(--blue);color:#fff;font-size:13px;padding:13px 19px;text-decoration:none}
.promo{height:40px;background:var(--blue);color:#fff;font-size:12px;font-weight:500;display:flex;align-items:center;justify-content:center;gap:18px}
.header{height:102px;border-bottom:2px solid #333;position:relative}
.header > *{position:absolute;top:50%;transform:translateY(-50%)}
.logo{font-family:'Alice',serif;color:var(--blue);font-size:38px}
.header .logo{left:112px}
.nav{left:371px;display:flex;gap:22px;font-size:14px;font-weight:500}
.nav a{color:var(--ink);text-decoration:none}
.nav a.active{color:var(--blue);text-decoration:underline}
.search{left:663px;width:233px;height:48px;border:1.5px solid #bbb;font-size:12px;color:#555;padding:0 10px;display:flex;align-items:center}
.lang{left:910px;width:113px;height:48px;border:1.5px solid #bbb;display:flex;align-items:center;justify-content:center;gap:8px;font-size:13px}
.flag{width:48px;height:28px;background:repeating-linear-gradient(#c33 0 4px,#fff 4px 8px);border:1px solid #ccc;position:relative}
.flag::before{content:"";position:absolute;left:0;top:0;width:20px;height:15px;background:#2a3d8f}
.cart{left:1040px;width:47px;height:47px;border:1.5px solid #bbb;border-radius:50%;display:flex;align-items:center;justify-content:center}
.hero{height:572px;position:relative}
.hero h1{position:absolute;left:108px;top:170px;font-family:'Alice',serif;font-size:96px;font-weight:400;line-height:1.1}
.hero p{position:absolute;left:111px;top:290px;width:520px;font-size:17px;line-height:30px}
.hero .btn{position:absolute;left:111px;top:384px;font-size:18px;padding:20px 24px}
.hero-art{position:absolute;left:655px;top:92px;width:432px;height:404px;border-radius:28px;
  background:linear-gradient(135deg,#e5484d 0%,#c9252b 18%,#5a6cc0 42%,#3f5bb8 55%,#2d2d2d 78%,#d83a3f 100%);opacity:.92}
.band{height:27px;background:var(--blue)}
.cards-sec{height:519px;position:relative}
.title-c{text-align:center;font-family:'Alice',serif;font-size:34px;font-weight:400;padding-top:68px}
.products{position:absolute;top:161px;left:112px;display:flex;gap:25px}
.product{width:224px;height:266px;border:1.5px solid #ccc;text-align:center}
.product.lift{box-shadow:0 3px 10px rgba(0,0,0,.25)}
.product .img{width:180px;height:104px;margin:40px auto 30px;border-radius:6px;background:linear-gradient(135deg,#fafafa,#ececec 45%,#f6d6d6 80%,#e9e9e9)}
.product.lift .img{background:linear-gradient(135deg,#f4f4f4,#5a6cc0 40%,#c9252b 60%,#f0f0f0)}
.product .name{font-size:16px;font-weight:500}
.product .price{font-size:17px;font-weight:600;color:var(--blue);margin-top:10px}
.split{height:428px;display:flex}
.split .half{width:600px;height:428px;position:relative}
.split h2{font-family:'Alice',serif;font-size:42px;font-weight:400}
.split p{font-size:13px;line-height:29px;color:#444;margin-top:18px;width:432px}
.split .btn{margin-top:20px;padding:15px 19px}
.video{background:linear-gradient(180deg,#8a8a86 0%,#6c6e5e 22%,#56603e 45%,#4a4a42 65%,#77776f 85%,#9a9893 100%)}
.play{position:absolute;left:255px;top:170px;width:90px;height:90px}
.photo-cards{background:linear-gradient(110deg,#d9d6cc 0%,#b9a78a 30%,#a66a38 55%,#7a4b2a 75%,#b7b9c0 100%)}
.faq{height:618px;position:relative}
.faq h2{position:absolute;left:112px;top:72px;font-family:'Alice',serif;font-size:42px;font-weight:400}
.faq-list{position:absolute;left:112px;top:142px;width:503px}
.faq-item{height:55px;border:2px solid #333;margin-bottom:14px;display:flex;align-items:center;justify-content:space-between;padding:0 14px 0 11px;font-size:15px}
.faq-text{position:absolute;left:653px;top:140px;width:434px;font-size:13px;line-height:26.5px;color:#555;text-align:justify}
.faq-text p{margin-bottom:6px}
.blog{height:573px;position:relative;background:radial-gradient(circle at 75% 45%,#2a7fce,#0b5aa8 50%,#0a4a8c)}
.blog h2{text-align:center;color:#fff;font-family:'Alice',serif;font-size:42px;font-weight:400;padding-top:78px}
.post{position:absolute;top:212px;display:flex;gap:18px;color:#fff}
.post .img{width:188px;height:263px;border:2px solid #fff}
.post h3{font-size:20px;font-weight:300;line-height:30px;margin-top:26px}
.post p{font-size:14px;font-weight:300;line-height:25px;margin-top:10px;width:272px}
.post .pill{display:inline-block;background:#fff;color:var(--blue);border-radius:26px;padding:11px 20px;font-size:17px;margin-top:24px}
.footer{position:relative;height:547px}
.footer .logo{position:absolute;left:112px;top:114px;font-size:52px}
.contact{position:absolute;left:112px;font-size:20px;font-weight:500;display:flex;gap:12px;align-items:flex-start;line-height:30px}
.contact .ic{width:50px;height:50px;border-radius:50%;background:var(--blue);display:flex;align-items:center;justify-content:center;flex:none}
.links{position:absolute;left:644px;top:110px}
.links h4,.signup h4{color:var(--blue);font-size:22px;font-weight:400}
.link-grid{display:grid;grid-template-columns:162px 120px;font-size:16px;line-height:26px;margin-top:8px}
.signup{position:absolute;left:644px;top:278px}
.signup form{display:flex;gap:10px;margin-top:10px}
.signup .field{width:304px;height:50px;border:1.5px solid #bbb;font-size:16px;padding:0 12px;display:flex;align-items:center}
.signup .submit{width:117px;height:50px;background:var(--blue);color:#fff;font-size:18px;font-weight:500;display:flex;align-items:center;justify-content:center}
.bottom{position:absolute;left:112px;right:112px;top:465px;border-top:1.5px solid #bbb}
.copy{position:absolute;left:112px;top:500px;font-size:16px}
.pay{position:absolute;left:738px;top:492px;display:flex;gap:4px}
.pay span{width:24px;height:16px;border-radius:3px;background:#c9d6e8}
.social{position:absolute;left:922px;top:486px;display:flex;gap:8px}
.social span{width:36px;height:36px;border:2px solid #333;border-radius:50%}
</style>
</head>
<body>
<div class="promo"><span>50% Off Flat Cards &amp; Invitations - Shop Now ›</span><span>Use Code: VELMOORJUNE</span></div>
<header class="header">
  <div class="logo">Velmoor</div>
  <nav class="nav"><a class="active" href="#">HOME</a><a href="#">ABOUT</a><a href="#">SHOP</a><a href="#">CONTACT</a></nav>
  <div class="search">Search</div>
  <div class="lang"><span class="flag"></span>EN <svg width="10" height="6"><path d="M0 0h10L5 6z" fill="#222"/></svg></div>
  <div class="cart"><svg width="20" height="22" viewBox="0 0 20 22" fill="none" stroke="#222" stroke-width="2"><rect x="2" y="7" width="16" height="13" rx="1"/><path d="M6 9V5a4 4 0 0 1 8 0v4"/></svg></div>
</header>
<section class="hero">
  <h1>Velmoor</h1>
  <p>Nemo enim ipsam voluptatem quia voluptas sit aspernatur aut odit aut fugit, sed quias.</p>
  <a class="btn" href="#">Read More</a>
  <div class="hero-art" role="img" aria-label="Illustration of a blue playing card framed by heart, spade, club and diamond suits"></div>
</section>
<div class="band"></div>
<section class="cards-sec">
  <h2 class="title-c">Playing Cards</h2>
  <div class="products">
    <div class="product"><div class="img" role="img" aria-label="Fan of four ace playing cards"></div><div class="name">Nemo Enim Ipsam</div><div class="price">$50.00</div></div>
    <div class="product lift"><div class="img" role="img" aria-label="Ace cards with flag-inspired card back"></div><div class="name">Nemo Enim Ipsam</div><div class="price">$50.00</div></div>
    <div class="product"><div class="img" role="img" aria-label="Fan of four ace playing cards"></div><div class="name">Nemo Enim Ipsam</div><div class="price">$50.00</div></div>
    <div class="product"><div class="img" role="img" aria-label="Fan of four ace playing cards"></div><div class="name">Nemo Enim Ipsam</div><div class="price">$50.00</div></div>
  </div>
</section>
<section class="split">
  <div class="half" style="padding:42px 0 0 112px">
    <h2>Why Velmoor</h2>
    <p>Nemo enim ipsam voluptatem quia voluptas sit aspernatur aut odit aut fugit, sed quia consequuntur magni dolores eos qui ra tione voluptatem sequi nesciunt. Neque porro quisquam est, qui dolorem ipsum quia dolor sit amet, consectetur, adipisci velit, sed quia non numquam eius modi tempora incidunt ut labore et dolore magnam aliquam quaerat.</p>
    <a class="btn" href="#">Read More</a>
  </div>
  <div class="half video" role="img" aria-label="Video still of a river flowing over rocks in green hills">
    <svg class="play" viewBox="0 0 90 90"><circle cx="45" cy="45" r="42" fill="none" stroke="#fff" stroke-width="5"/><path d="M36 28l26 17-26 17z" fill="#fff"/></svg>
  </div>
</section>
<section class="split">
  <div class="half photo-cards" role="img" aria-label="Photo of an elderly couple playing a tile game at a table"></div>
  <div class="half" style="padding:58px 0 0 56px">
    <h2>About Velmoor</h2>
    <p>Nemo enim ipsam voluptatem quia voluptas sit aspernatur aut odit aut fugit, sed quia consequuntur magni dolores eos qui ra tione voluptatem sequi nesciunt. Neque porro quisquam est, qui dolorem ipsum quia dolor sit amet, consectetur, adipisci velit, sed quia non numquam eius modi tempora incidunt ut labore et dolore magnam aliquam quaerat.</p>
    <a class="btn" href="#">Read More</a>
  </div>
</section>
<section class="faq">
  <h2>Our FAQ</h2>
  <div class="faq-list">
    <div class="faq-item">Nemo enim ipsam voluptatem quia voluptas? <svg width="7" height="11"><path d="M0 0l7 5.5L0 11z" fill="#222"/></svg></div>
    <div class="faq-item">Ut enim ad minima veniam, quis nostrum exercitationem? <svg width="11" height="7"><path d="M0 0h11L5.5 7z" fill="#222"/></svg></div>
    <div class="faq-item">Nemo enim ipsam voluptatem quia voluptas? <svg width="11" height="7"><path d="M0 0h11L5.5 7z" fill="#222"/></svg></div>
    <div class="faq-item">Ade minima veniam, quis nostrum exercitationem? <svg width="11" height="7"><path d="M0 0h11L5.5 7z" fill="#222"/></svg></div>
    <div class="faq-item">Nemo enim ipsam voluptatem quia voluptas? <svg width="11" height="7"><path d="M0 0h11L5.5 7z" fill="#222"/></svg></div>
    <div class="faq-item">Ad minima veniam, quis nostrum exercitationem? <svg width="11" height="7"><path d="M0 0h11L5.5 7z" fill="#222"/></svg></div>
  </div>
  <div class="faq-text">
    <p>Sed ut perspiciatis unde omnis iste natus error sit voluptatem accusantium doloremque laudantium, totam rem aperiam, eaque ipsa quae ab illo inventore veritatis et quasi architecto beatae vitae dicta sunt explicabo. Nemo enim ipsam voluptatem quia voluptas.</p>
    <p>Nemo enim ipsam voluptatem quia voluptas sit aspernatur aut odit aut fugit, sed quia consequuntur magni dolores eos qui ratione voluptatem sequi nesciunt. Neque porro quisquam est, qui dolorem ipsum quias.</p>
    <p>Your disability insurance policy must define you as disabled if a sickness or injury makes it so you are no longer able, or you are no longer comfortable, working as a physician – and it should not penalize you if you engage in another occupation.</p>
  </div>
</section>
<section class="blog" role="region" aria-label="Blog posts over a blurred playing card background">
  <h2>Our Blog Posts</h2>
  <div class="post" style="left:112px">
    <div class="img" role="img" aria-label="Hands holding a fan of playing cards" style="background:linear-gradient(135deg,#cdb59d,#f1ece6 45%,#e7c9b0 70%,#b98a66)"></div>
    <div><h3>Nam libero tempore, cum<br>soluta nobis est</h3><p>At vero eos et accusamus et iusto odio dignissimos ducimus qui blanditiis praesentium voluptatum</p><span class="pill">Read More</span></div>
  </div>
  <div class="post" style="left:615px">
    <div class="img" role="img" aria-label="Older man holding playing cards" style="background:linear-gradient(135deg,#ece8e0,#c5cedb 40%,#8ea3c4 65%,#d3b29a)"></div>
    <div><h3>Nam libero tempore, cum<br>soluta nobis est</h3><p>At vero eos et accusamus et iusto odio dignissimos ducimus qui blanditiis praesentium voluptatum</p><span class="pill" style="margin-top:32px">Read More</span></div>
  </div>
</section>
<footer class="footer">
  <div class="logo">Velmoor</div>
  <div class="contact" style="top:230px"><span class="ic"><svg width="24" height="24" viewBox="0 0 24 24"><path d="M6 3l3 4-2 2a11 11 0 0 0 8 8l2-2 4 3-2 3C11 21 3 13 3 5z" fill="#fff"/></svg></span><span style="padding-top:10px">+268 7600 4210, +1 (555) 014-2290</span></div>
  <div class="contact" style="top:290px"><span class="ic"><svg width="22" height="16" viewBox="0 0 22 16" fill="none" stroke="#fff" stroke-width="2"><rect x="1" y="1" width="20" height="14"/><path d="M1 1l10 8 10-8"/></svg></span><span style="padding-top:10px">hello@velmoorcards.example</span></div>
  <div class="contact" style="top:350px"><span class="ic"><svg width="18" height="24" viewBox="0 0 18 24" fill="none" stroke="#fff" stroke-width="2"><path d="M9 23S2 14 2 9a7 7 0 0 1 14 0c0 5-7 14-7 14z"/><circle cx="9" cy="9" r="2.5"/></svg></span><span>480 Harbor Lantern Road - Suite 9<br>Millbrook, ST 00000</span></div>
  <div class="links"><h4>Links</h4>
    <div class="link-grid"><span>About</span><span>Home</span><span>Careers</span><span>About</span><span>Return Policy</span><span>Contact</span><span>Contact</span></div>
  </div>
  <div class="signup"><h4>EMAIL SIGNUP</h4>
    <form><div class="field">Enter Your Email</div><div class="submit">Submit</div></form>
  </div>
  <div class="bottom"></div>
  <div class="copy">Copyrights @ 2020 Velmoor. All Rights Reserved.</div>
  <div class="pay"><span></span><span></span><span></span><span></span><span></span></div>
  <div class="social"><span></span><span></span><span></span><span></span></div>
</footer>
</body>
</html>
```